Business card New design- upscale

Looking for modern design business cards. Minimalist, mix of gloss and matte finishes. Texas based Contractor company doing Mechanical hvac and plumbing, focused on commercial and industrial manufacturing facilities. We don't hand too many out so high end materials or functionality...will be considered. Please see attached files for info needed on cards. *New plumbing license needs to be edited to say K82917. Www.valtrimgroup.com
P.s. Website will also be redesigned soon.

Target Market(s)

Facility managers for commercial buildings, mechanical engineers for industrial manufacturing facilities including pharmaceutical, semiconductor, food & beverage, etc

Contact Information for Business Card

See attached images

Requirements
Must have
• All Logo colors: purple, black and Gray. 1, 2 or 4 rounded corners. All content on existing business cards (see attached images).
Nice to have
• Matte and gloss print. Embossing, raised print, functionality.
Should not have
• Stock images, generic construction.

```html
<!DOCTYPE html>
<html lang="en">
<head>
<meta charset="utf-8">
<title>Valtrim Group Business Card</title>
<link rel="stylesheet" href="https://fonts.googleapis.com/css2?family=Arimo:ital,wght@0,400;0,700;1,400&family=Michroma&family=Syncopate:wght@700&display=swap">
<style>
  :root {
    --backdrop: #2a2a2c;
    --purple-deep: #3a1f5c;
    --purple-light: #5e4190;
    --brand-purple: #3b2266;
    --white: #ffffff;
    --card-light: #ffffff;
    --card-shade: #dcdcdc;
    --ink: #333333;
    --ink-soft: #4a4a4a;
    --rule-light: #c8c8c8;
  }
  * { margin: 0; padding: 0; box-sizing: border-box; }
  html, body { width: 1093px; height: 1200px; overflow: hidden; }
  body {
    background: var(--backdrop);
    font-family: "Arimo", Arial, sans-serif;
    position: relative;
  }
  .card {
    position: absolute;
    left: 264px;
    height: 357px;
    box-shadow: 3px 4px 6px rgba(0,0,0,0.6);
  }
  .card-front {
    top: 226px;
    width: 578px;
    background: linear-gradient(225deg, var(--purple-light) 0%, var(--purple-deep) 100%);
    color: var(--white);
  }
  .card-back {
    top: 620px;
    width: 582px;
    background: linear-gradient(225deg, var(--card-light) 30%, var(--card-shade) 100%);
    color: var(--ink);
  }
  .line {
    position: absolute;
    left: 0;
    width: 100%;
    text-align: center;
    white-space: nowrap;
    line-height: 1;
  }
  .rule {
    position: absolute;
    left: 50%;
    height: 1px;
    transform: translateX(-50%);
  }
  .card-front .rule { width: 134px; background: var(--white); }
  .card-back .rule { width: 142px; background: var(--rule-light); }

  .person-name {
    font-family: "Syncopate", sans-serif;
    font-weight: 700;
    font-size: 15px;
    letter-spacing: 2px;
  }
  .person-title { font-size: 16.5px; }
  .contact { font-size: 16.5px; }
  .contact b { font-weight: 700; }
  .tagline { font-size: 16px; font-style: italic; }

  .brand-name {
    font-family: "Michroma", sans-serif;
    font-size: 26px;
    color: var(--brand-purple);
    letter-spacing: 1px;
  }
  .license-no { font-size: 17px; color: var(--ink-soft); }
  .regulator { font-size: 14.6px; color: var(--ink); }
</style>
</head>
<body>
  <section class="card card-front">
    <div class="line person-name" style="top:53px;">DALE HARMON</div>
    <div class="line person-title" style="top:72px;">Lead Estimator/Sr.Project Manager</div>
    <div class="rule" style="top:95px;"></div>
    <div class="line contact" style="top:109px;"><b>P:</b> (817) 555-0148</div>
    <div class="line contact" style="top:130px;"><b>M:</b> (520)555-0193</div>
    <div class="line contact" style="top:151px;"><b>E:</b>dharmon@valtrimgroup.com</div>
    <div class="line contact" style="top:172px;">www.valtrimgroup.com</div>
    <div class="rule" style="top:196px;"></div>
    <div class="line contact" style="top:205px;">2180 Ridgeline Crossing Rd.</div>
    <div class="line contact" style="top:226px;">Fort Worth, TX 76119</div>
    <div class="rule" style="top:252px;"></div>
    <div class="line tagline" style="top:268px;">Commercial &amp; Industrial Contractors</div>
    <div class="line tagline" style="top:287px;">Mechanical &amp; Plumbing Services</div>
  </section>

  <section class="card card-back">
    <div class="line brand-name" style="top:68px;">VALTRIM GROUP</div>
    <div class="line license-no" style="top:143px;">LIC No. K82917</div>
    <div class="line regulator" style="top:200px;">M-30217 Regulated by the Lone Star Board of Pipe Trade Examiners</div>
    <div class="line regulator" style="top:218px;">P.O. Box 5310, Austin,TX. 78760</div>
    <div class="line regulator" style="top:236px;">1-800-555-0172, 512-555-0136</div>
    <div class="rule" style="top:262px;"></div>
    <div class="line regulator" style="top:271px;">TACLA50318B Regulated by the Lone Star Office of Trade Licensing and Review</div>
    <div class="line regulator" style="top:289px;">P.O. Box 10482, Austin, TX. 78714</div>
    <div class="line regulator" style="top:308px;">1-800-555-0124, 512-555-0187</div>
    <div class="line regulator" style="top:326px;">www.txtradelicense.org</div>
  </section>
</body>
</html>
```